Business Card Design Project

I need a business card design for a new business called Thornal Insurance Services. I am a small insurance broker that will provide business insurance services mostly to contractors and small businesses. My business is all about customer service and assistance rather than being a price driven/focused business. I want my business card to be professional giving the impression that I am larger than one person but not a corporate company. I have attached a copy of my logo.
Updates

Hi all

I have been advised that I need to show the following info for compliance reasons on my card. It only has to be small.

Can you please include either front or back:

Thornal Insurance Services Pty Ltd [ABN 61728405913] AR No 586027 as Authorised Representative of Carrodine Insurance Group Pty Ltd ACN 274 619 508 ABN 82 274 619 508 AFS Licence No 718246

Reason: I need a further change to be made to the design. I need the contact number of 1300584619 added to the business card.

Hi All

I need one last change made to the card.

Can you please include the phone number 1300584619 to the card. If possible can this be made fairly clear on the card, either large on the back or another design idea you may have.

Target Market(s)

30+ Professionals

Industry/Entity Type

Insurance

Requirements
Must have
• I want a double sided design. My details to go on the card are as follows:

Dean Thornal QRTMOL (Snr Assoc.) CIP
Director
PO Box 782, Fernmoor SA 5071
Phone: 0438 612 704
Fax 08 8347 2910
Email: dean@thornalcover.example.au
Website: http://www.thornalcover.example.au
Twitter: Thornalcover
Facebook: facebook.com/thornalcover

```html
<!DOCTYPE html>
<html lang="en">
<head>
<meta charset="utf-8">
<title>Thornal Insurance Services – Business Card</title>
<link rel="stylesheet" href="https://fonts.googleapis.com/css2?family=Questrial&display=swap">
<style>
  :root {
    --stage: #2e2b29;
    --card-front: #ffffff;
    --card-back: #dedede;
    --ink: #1e1e1e;
    --ink-soft: #3a3a3a;
    --muted: #8a8a8a;
    --rule: #c4c4c4;
    --accent: #d7261e;
    --pill: #2b2b2b;
  }
  * { margin: 0; padding: 0; box-sizing: border-box; }
  html, body { width: 1200px; height: 846px; overflow: hidden; }
  body {
    background: var(--stage);
    font-family: "Questrial", "Century Gothic", sans-serif;
    color: var(--ink);
    position: relative;
  }
  .card {
    position: absolute;
    left: 169px;
    width: 508px;
    height: 290px;
  }
  .card--front { top: 106px; background: var(--card-front); }
  .card--back { top: 461px; background: var(--card-back); }

  /* Front */
  .tagline {
    position: absolute; left: 37px; top: 46px;
    font-size: 24px; line-height: 33px; color: var(--ink);
  }
  .tagline__accent { display: block; color: var(--accent); font-size: 32px; line-height: 36px; }
  .brand-small {
    position: absolute; right: 30px; top: 44px;
    display: flex; align-items: center; gap: 6px;
    font-size: 15px; color: var(--ink);
  }
  .dot { width: 9px; height: 9px; border-radius: 50%; background: var(--accent); }
  .person {
    position: absolute; right: 30px; top: 118px; text-align: right;
  }
  .person__name { font-size: 22px; color: var(--ink); margin-bottom: 6px; }
  .person__role { font-size: 12.5px; letter-spacing: 0.6px; color: var(--ink-soft); line-height: 17px; }
  .card__rule {
    position: absolute; left: 36px; right: 30px; top: 196px;
    height: 2px; background: var(--rule);
  }
  .hotline {
    position: absolute; left: 34px; top: 225px;
    width: 180px; height: 28px;
    background: var(--pill); border-radius: 14px;
    display: flex; align-items: center;
  }
  .hotline__icon {
    width: 34px; height: 34px; margin-left: -1px;
    border-radius: 50%; background: var(--accent);
    border: 3px solid var(--card-front);
    display: flex; align-items: center; justify-content: center;
  }
  .hotline__number { color: #fff; font-size: 17px; letter-spacing: 1px; margin-left: 12px; }
  .contacts {
    position: absolute; right: 30px; top: 208px; text-align: right;
    font-size: 10.5px; letter-spacing: 1px; line-height: 17px; color: var(--ink-soft);
  }

  /* Back */
  .brand {
    position: absolute; left: 0; right: 0; top: 96px;
    display: flex; justify-content: center; align-items: center; gap: 12px;
  }
  .brand__dot { width: 14px; height: 14px; border-radius: 50%; background: var(--accent); }
  .brand__text { display: flex; flex-direction: column; align-items: center; }
  .brand__name { font-size: 27px; color: var(--ink); line-height: 30px; }
  .brand__line {
    display: flex; align-items: center; gap: 6px;
    font-size: 8.5px; letter-spacing: 1.4px; color: var(--ink-soft);
  }
  .brand__line::before, .brand__line::after {
    content: ""; width: 20px; height: 1px; background: var(--ink-soft);
  }
  .brand__line em { font-style: normal; color: var(--accent); }
  .social {
    position: absolute; left: 28px; right: 28px; top: 209px;
    height: 27px;
    border-top: 2px solid var(--rule); border-bottom: 2px solid var(--rule);
    display: flex; justify-content: space-between; align-items: center;
    font-size: 11px; letter-spacing: 0.5px; color: var(--ink-soft);
  }
  .social__item { display: flex; align-items: center; gap: 7px; }
  .social__mark { width: 10px; height: 10px; background: var(--ink-soft); }
  .legal {
    position: absolute; left: 0; right: 0; top: 244px;
    text-align: center; font-size: 7.4px; letter-spacing: 0.5px;
    line-height: 11px; color: var(--muted);
  }
</style>
</head>
<body>

<section class="card card--front" aria-label="Card front">
  <p class="tagline">Insurance<br>Advice<br>You Can<span class="tagline__accent">Trust</span></p>
  <div class="brand-small"><span class="dot"></span>thornal</div>
  <div class="person">
    <p class="person__name">Dean Thornal</p>
    <p class="person__role">QRTMOL (Snr Assoc.) CIP<br>Director</p>
  </div>
  <div class="card__rule"></div>
  <div class="hotline">
    <span class="hotline__icon">
      <svg width="14" height="14" viewBox="0 0 24 24" aria-hidden="true">
        <path fill="#fff" d="M6.6 10.8a15.1 15.1 0 0 0 6.6 6.6l2.2-2.2a1 1 0 0 1 1-.25 11.4 11.4 0 0 0 3.6.57 1 1 0 0 1 1 1V20a1 1 0 0 1-1 1A17 17 0 0 1 3 4a1 1 0 0 1 1-1h3.5a1 1 0 0 1 1 1c0 1.25.2 2.45.57 3.57a1 1 0 0 1-.25 1z"/>
      </svg>
    </span>
    <span class="hotline__number">1300 584 619</span>
  </div>
  <div class="contacts">
    <p>dean@thornalcover.example.au</p>
    <p>TEL: 0438 612 704</p>
    <p>FAX: 08 8347 2910</p>
  </div>
</section>

<section class="card card--back" aria-label="Card back">
  <div class="brand">
    <span class="brand__dot"></span>
    <div class="brand__text">
      <span class="brand__name">thornal insurance</span>
      <span class="brand__line">Insurance advice you can <em>trust</em></span>
    </div>
  </div>
  <div class="social">
    <span class="social__item"><span class="social__mark"></span>Thornalcover</span>
    <span class="social__item"><span class="social__mark"></span>Thornalcover</span>
    <span class="social__item">
      <svg width="12" height="12" viewBox="0 0 12 12" aria-hidden="true" fill="none" stroke="#3a3a3a" stroke-width="1">
        <circle cx="6" cy="6" r="5"/><ellipse cx="6" cy="6" rx="2.2" ry="5"/><line x1="1" y1="6" x2="11" y2="6"/>
      </svg>
      www.thornalcover.example.au
    </span>
  </div>
  <p class="legal">Thornal Insurance Services Pty Ltd [ABN 61728405913] AR No 586027 as Authorised Representative<br>of Carrodine Insurance Group Pty Ltd ACN 274 619 508 ABN 82 274 619 508 AFS Licence No 718246</p>
</section>

</body>
</html>
```